Tavrel Software Overview Brochure

Tavrel Software has developed a cloud based accounting systems for small businesses that have out grown products like Brindlepath. We need an overview brochure that can be delivered in a PDF and become incorporated into our web site. I have attached our logo as a reference for colors and style.

The brochure should be speak to small business owners and communicate why Tavrel is better for them than Brindlepath. I will be happy to provide screen shots and content.

Target Market(s)

companies between 10 and 200 employees

Industry/Entity Type

Small Business

Requirements
Must have
• Strong branding around the Tavrel name and logo. Room for screen shots of the software and discussion of product features.

```html
<!DOCTYPE html>
<html lang="en">
<head>
<meta charset="utf-8">
<title>Tavrel Software Overview Brochure</title>
<link rel="stylesheet" href="https://fonts.googleapis.com/css2?family=Ubuntu:wght@400;500;700&family=Open+Sans:wght@400&display=swap">
<style>
  :root {
    --backdrop: #d6d6d6;
    --brand-red: #c40b12;
    --brand-red-deep: #7a0006;
    --ink: #222222;
    --ink-soft: #555555;
    --paper: #ffffff;
    --paper-shade: #e4e4e4;
    --photo-light: #eef2f4;
    --photo-mid: #c9d1d6;
  }
  html, body {
    margin: 0;
    width: 1200px;
    height: 800px;
    overflow: hidden;
    background: var(--backdrop);
  }
  .brochure-spread {
    position: absolute;
    left: 200px;
    top: 110px;
    width: 800px;
    height: 580px;
    box-shadow: 0 14px 30px rgba(0,0,0,0.25);
  }
  .spread-art {
    position: absolute;
    inset: 0;
    display: block;
  }
  .back-panel, .front-panel {
    position: absolute;
    top: 0;
    width: 400px;
    height: 580px;
  }
  .back-panel { left: 0; }
  .front-panel { left: 400px; }

  .intro-heading {
    position: absolute;
    left: 32px;
    top: 36px;
    margin: 0;
    font: 700 11.5px/1 "Ubuntu", sans-serif;
    color: var(--paper);
  }
  .intro-body {
    position: absolute;
    left: 32px;
    top: 59px;
    margin: 0;
    font: 400 9.6px/13.05px "Ubuntu", sans-serif;
    color: var(--paper);
    white-space: nowrap;
  }
  .contact-block {
    position: absolute;
    right: 22px;
    top: 508px;
    margin: 0;
    text-align: right;
    font: 400 13.5px/19px "Open Sans", sans-serif;
    color: var(--ink);
  }
  .brand-lockup {
    position: absolute;
    left: 162px;
    top: 410px;
    display: flex;
    align-items: center;
    gap: 10px;
  }
  .brand-dot {
    width: 40px;
    height: 40px;
    border-radius: 50%;
    background: var(--brand-red);
  }
  .brand-name {
    font: 500 22px/22px "Ubuntu", sans-serif;
    color: var(--brand-red);
    letter-spacing: 1px;
    text-transform: uppercase;
  }
  .brand-tagline {
    position: absolute;
    left: 162px;
    top: 478px;
    margin: 0;
    font: 400 16px/15px "Ubuntu", sans-serif;
    color: var(--ink-soft);
  }
</style>
</head>
<body>
<main class="brochure-spread">
  <svg class="spread-art" viewBox="0 0 800 580" width="800" height="580">
    <defs>
      <linearGradient id="photoTone" x1="0" y1="0" x2="1" y2="0">
        <stop offset="0" stop-color="var(--photo-mid)"/>
        <stop offset="0.5" stop-color="var(--photo-light)"/>
        <stop offset="1" stop-color="var(--photo-mid)"/>
      </linearGradient>
      <linearGradient id="redSweep" x1="0" y1="0" x2="1" y2="0">
        <stop offset="0" stop-color="var(--brand-red)"/>
        <stop offset="0.6" stop-color="var(--brand-red)"/>
        <stop offset="1" stop-color="var(--brand-red-deep)"/>
      </linearGradient>
      <linearGradient id="paperTone" x1="0" y1="0" x2="1" y2="1">
        <stop offset="0" stop-color="var(--paper)"/>
        <stop offset="1" stop-color="var(--paper-shade)"/>
      </linearGradient>
      <linearGradient id="foldShade" x1="0" y1="0" x2="1" y2="0">
        <stop offset="0" stop-color="#000" stop-opacity="0.12"/>
        <stop offset="1" stop-color="#000" stop-opacity="0"/>
      </linearGradient>
    </defs>
    <rect class="office-photo" x="0" y="0" width="800" height="580" fill="url(#photoTone)"
          role="img" aria-label="Photo of business people walking through a bright office corridor"/>
    <path class="red-sweep" d="M0 0 H800 V16 C640 48 490 120 410 196 C310 284 130 372 0 492 Z" fill="url(#redSweep)"/>
    <path class="lower-paper" d="M40 580 C200 500 420 430 800 328 V580 Z" fill="url(#paperTone)"/>
    <path class="accent-curve" d="M40 580 C200 500 420 430 800 328" fill="none" stroke="var(--brand-red)" stroke-width="7"/>
    <rect class="fold-shade" x="400" y="0" width="40" height="580" fill="url(#foldShade)"/>
  </svg>

  <section class="back-panel">
    <h2 class="intro-heading">Lorem ipsum dolor sit amet</h2>
    <p class="intro-body">Lorem ipsum dolor sit amet. Lorem sanctus stet. Est kasd sed clita. Commodo<br>
et liber sit nisl. Ea amet et sed. Iriure eu commodo aliquip. Lorem eirmod<br>
labore. Diam tation takimata nam elitr diam eos. Diam kasd tempor et.<br>
Gubergren mazim vero gubergren eirmod te gubergren justo.<br>
At takimata diam dolor et aliquam sea. Amet vero diam labore. Duo clita<br>
eirmod minim nobis dolores hendrerit. Est luptatum sit gubergren amet iriure.<br>
Nonummy sanctus eu amet. Sadipscing in sit eirmod takimata lorem stet. Eos<br>
aliquyam lorem takimata elitr magna eirmod. Sit suscipit amet. Et euismod<br>
amet. Elitr ut lorem. Tempor vel dolores sit eirmod dolore. Accusam cum<br>
dolores et nonumy amet. Eirmod sanctus est nonummy kasd. Wisi lorem<br>
sadipscing. Nonumy magna diam amet eu nihil sit et. Et stet lorem.<br>
Magna blandit diam est esse est possim. Clita lobortis duis ipsum kasd duis<br>
consetetur. Diam magna ipsum ullamcorper sadipscing clita.<br>
Et magna sea rebum wisi euismod diam justo. Lorem erat<br>
luptatum et. Eum duo magna. Eos vero consetetur est.<br>
Kasd consequat dolores ea vero dignissim.<br>
Nonummy assum dolores amet ipsum wisi. Clita<br>
suscipit sed eros sanctus assum imperdiet<br>
vero. Dolore tempor sea. Augue et vel et<br>
consequat sed. Est vel ipsum sed.</p>
    <p class="contact-block">+1 555 0142 7788<br>
info@tavrelsoftware.com<br>
www.tavrelsoftware.com</p>
  </section>

  <section class="front-panel">
    <div class="brand-lockup">
      <span class="brand-dot"></span>
      <span class="brand-name">Tavrel<br>Software</span>
    </div>
    <p class="brand-tagline">a cloud based<br>accounting systems</p>
  </section>
</main>
</body>
</html>
```